Vantor Cleaners Postcard - I would like to send this using MAIL to my prospects and current clients.

This store is under new management. I would like to design a high end postcard that showcases our services. Here is a list of the services that we provide to our customers.
- Premium Organic Dry Cleaning
- Laundered Shirts
- Expert Alterations
- Shoes and Leather Repairs by Pelham Brothers
- Area Rug Cleaning by Tarrick Cleaners
- Leather and Suede Cleaning by Mosk Cleaners
- Household Items
- Wedding Dress Cleaning and Preservation
I would like to offer 10% off (one-time use) coupon as well as 20% off to new customers.
Here is a logo file with location details.
While designing postcards, I would like to showcase stack of different garments (Season based) and household items. Also, use the colors that I have provided in the logo design.
We also offer Free Pick up and delivery.
About Us:
Vantor Cleaners is a premium dry cleaning and garment care service dedicated to delivering exceptional quality, convenience, and personalized attention. Located in the heart of Corwin Falls, NJ, we specialize in eco-friendly dry cleaning, expert stain removal, professional garment pressing, and specialized care for delicate fabrics, designer clothing, household items, and formal wear.
Our mission is to provide reliable, high-quality service while preserving the longevity and appearance of our customers’ garments. With state-of-the-art equipment, experienced staff, and a commitment to customer satisfaction, Vantor Cleaners ensures your clothing looks and feels its best — every time.
We also offer convenient services such as same-day cleaning, alterations, wash & fold, and pickup and delivery options, making garment care simple and hassle-free for our busy clientele.
Experience the difference with Vantor Cleaners — where luxury care meets everyday convenience.

Target Market(s)

Household above $100K

Industry/Entity Type

Dry Cleaning

Font styles to use
Serif

Colors
0054AA
0677BA
7BADD7
CADEEF
E8F1F8
FFC000
F8CF3A
FAE287
FDF2CF
FEFAEE

Requirements
Must have
• Elegant Design with stacked clothes, highlight Organic Dry Cleaning store. The color schemes should have these colors. D4AF37 (Fonts), 0D1B2A (Background). These are used in my logo and tagline.
Nice to have
• On the backside I would like to show our location on the map, streets

```html
<!DOCTYPE html>
<html lang="en">
<head>
<meta charset="utf-8">
<title>Vantor Cleaners Postcard</title>
<link rel="stylesheet" href="https://fonts.googleapis.com/css2?family=Cinzel:wght@600;700&family=Libre+Caslon+Text:wght@400;700&family=Poppins:wght@400;500;600&family=Rubik:wght@600;800;900&display=swap">
<style>
  :root {
    --navy: #0d1b2a;
    --gold: #d4af37;
    --gold-deep: #c9a227;
    --white: #ffffff;
    --stage: #e4e4e4;
  }
  * { margin: 0; padding: 0; box-sizing: border-box; }
  html, body { width: 1131px; height: 1200px; overflow: hidden; }
  body { background: var(--stage); position: relative; font-family: "Poppins", sans-serif; color: var(--navy); }

  .card { position: absolute; left: 145px; width: 840px; height: 560px; overflow: hidden; background: var(--white); box-shadow: 0 4px 14px rgba(0,0,0,.12); }
  .card-front { top: 27px; }
  .card-back { top: 613px; }
  .card svg.shapes { position: absolute; inset: 0; }
  .abs { position: absolute; }

  /* Front */
  .brand { left: 0; top: 52px; width: 250px; text-align: center; }
  .brand-name { font-family: "Cinzel", serif; font-weight: 600; color: var(--gold); font-size: 34px; line-height: 36px; letter-spacing: 1px; }
  .brand-tagline { font-family: "Libre Caslon Text", serif; color: var(--gold); font-size: 11.5px; margin-top: 2px; }
  .brand-address { font-family: "Libre Caslon Text", serif; color: var(--gold); font-size: 11px; line-height: 16px; margin-top: 10px; }

  .headline { left: 20px; top: 222px; font-family: "Cinzel", serif; font-weight: 700; color: var(--gold); font-size: 39px; line-height: 38px; }

  .offer-badge { left: 270px; top: 58px; width: 168px; text-align: center; line-height: 1; }
  .offer-small { font-weight: 600; font-size: 13px; color: var(--navy); }
  .offer-free { font-family: "Rubik", sans-serif; font-weight: 900; font-size: 34px; color: var(--gold); letter-spacing: 1px; margin-top: 1px; }

  .service-list { left: 20px; top: 322px; list-style: none; }
  .service-list li { font-size: 14.5px; line-height: 21.6px; display: flex; align-items: center; gap: 12px; }
  .service-list svg { width: 18px; height: 14px; flex: none; }

  .coupon { left: 432px; top: 332px; color: var(--white); font-weight: 600; font-size: 14.5px; line-height: 17px; }
  .coupon-title { font-family: "Rubik", sans-serif; font-weight: 800; color: var(--gold); font-size: 19px; margin-bottom: 12px; }
  .coupon-value { font-family: "Rubik", sans-serif; font-weight: 900; color: var(--gold); font-size: 19px; line-height: 18px; }
  .coupon-gap { height: 14px; }

  .phone-tab { left: 18px; top: 516px; display: flex; align-items: center; gap: 8px; font-family: "Rubik", sans-serif; font-weight: 800; font-size: 23px; color: var(--navy); }
  .phone-tab svg { width: 20px; height: 20px; }

  /* Back */
  .about-title { left: 20px; top: 22px; font-family: "Libre Caslon Text", serif; font-weight: 700; font-size: 31px; color: var(--navy); }
  .about-copy { left: 20px; top: 72px; width: 368px; font-size: 14.4px; line-height: 15.3px; color: var(--white); }
  .about-copy p + p { margin-top: 8px; }
  .call-label { left: 0; top: 455px; width: 150px; height: 30px; background: var(--navy); color: var(--white); border-radius: 0 15px 15px 0; font-family: "Rubik", sans-serif; font-weight: 800; font-size: 19px; line-height: 30px; padding-left: 18px; }
  .call-number { left: 18px; top: 494px; display: flex; align-items: center; gap: 10px; font-family: "Rubik", sans-serif; font-weight: 800; font-size: 33px; color: var(--navy); }
  .call-number svg { width: 30px; height: 30px; }

  .stamp-box { left: 686px; top: 17px; width: 134px; height: 126px; border: 1px solid var(--navy); }
  .address-line { left: 496px; width: 324px; height: 1px; background: var(--navy); }
  .map-address { left: 643px; top: 304px; font-weight: 600; font-size: 12px; line-height: 14.5px; }
  .map-area { left: 420px; top: 356px; width: 400px; height: 188px; background: linear-gradient(180deg, #d9d9d9, #b9b9b9); }
</style>
</head>
<body>

<section class="card card-front" aria-label="Postcard front">
  <svg class="shapes" viewBox="0 0 840 560">
    <defs>
      <linearGradient id="rackTone" x1="0" y1="0" x2="1" y2="1">
        <stop offset="0" stop-color="#1f2c48"/>
        <stop offset=".45" stop-color="#6d7d9c"/>
        <stop offset=".75" stop-color="#c9ccd2"/>
        <stop offset="1" stop-color="#eeeeee"/>
      </linearGradient>
      <linearGradient id="stackTone" x1="0" y1="0" x2="0" y2="1">
        <stop offset="0" stop-color="#1f6f6a"/>
        <stop offset=".3" stop-color="#c45a5a"/>
        <stop offset=".55" stop-color="#cdb98a"/>
        <stop offset=".8" stop-color="#8c95a3"/>
        <stop offset="1" stop-color="#2e4470"/>
      </linearGradient>
    </defs>
    <rect x="270" y="0" width="570" height="340" fill="url(#rackTone)" role="img" aria-label="Photo of a clothes rail with shirts and jackets on hangers"/>
    <g aria-hidden="true">
      <path d="M0 0 H262 L250 140 L262 215 H520 L470 300 H0 Z" fill="var(--navy)"/>
      <path d="M262 0 H282 L276 52 H268 Z M268 120 H276 L252 152 Z" fill="var(--white)"/>
      <rect x="268" y="50" width="170" height="74" rx="6" fill="var(--white)"/>
      <g stroke="var(--white)" stroke-width="6" stroke-linecap="round">
        <line x1="440" y1="62" x2="478" y2="62"/>
        <line x1="440" y1="78" x2="462" y2="78"/>
        <line x1="440" y1="94" x2="470" y2="94"/>
        <line x1="440" y1="110" x2="480" y2="110"/>
      </g>
      <path d="M0 310 H480 Q520 300 540 280 Q600 345 700 335 Q780 325 840 290 V560 H0 Z" fill="var(--white)"/>
      <rect x="320" y="300" width="240" height="10" fill="var(--gold)"/>
      <path d="M600 300 Q730 315 840 240 V285 Q740 340 600 320 Z" fill="var(--navy)"/>
      <path d="M510 262 Q560 335 640 338 Q750 340 840 290 V335 Q740 380 630 362 Q545 345 510 262 Z" fill="var(--gold)"/>
      <rect x="418" y="318" width="212" height="182" rx="18" fill="var(--navy)"/>
    </g>
    <rect x="612" y="268" width="185" height="278" rx="8" fill="url(#stackTone)" role="img" aria-label="Photo of a tall stack of folded seasonal garments"/>
    <g aria-hidden="true">
      <path d="M0 505 H225 Q238 505 238 518 V560 H0 Z" fill="var(--gold)"/>
      <rect x="238" y="551" width="252" height="9" fill="var(--navy)"/>
    </g>
  </svg>

  <div class="abs brand">
    <div class="brand-name">Vantor<br>Cleaners</div>
    <div class="brand-tagline">Luxury Care For Your Finest Wear</div>
    <div class="brand-address">18 Linden Ridge Road<br>Corwin Falls, NJ 07990</div>
  </div>

  <div class="abs offer-badge">
    <div class="offer-small">NOW OFFERING</div>
    <div class="offer-free">FREE</div>
    <div class="offer-small">PICKUP &amp; DELIVERY!</div>
  </div>

  <h1 class="abs headline">Organic Dry<br>Cleaning Store.</h1>

  <ul class="abs service-list">
    <li><svg viewBox="0 0 18 14"><path d="M1 8 L6 12 L17 2" fill="none" stroke="var(--gold)" stroke-width="2.4" stroke-linecap="round" stroke-linejoin="round"/></svg>Premium Organic Dry Cleaning</li>
    <li><svg viewBox="0 0 18 14"><path d="M1 8 L6 12 L17 2" fill="none" stroke="var(--gold)" stroke-width="2.4" stroke-linecap="round" stroke-linejoin="round"/></svg>Laundered Shirts</li>
    <li><svg viewBox="0 0 18 14"><path d="M1 8 L6 12 L17 2" fill="none" stroke="var(--gold)" stroke-width="2.4" stroke-linecap="round" stroke-linejoin="round"/></svg>Expert Alterations</li>
    <li><svg viewBox="0 0 18 14"><path d="M1 8 L6 12 L17 2" fill="none" stroke="var(--gold)" stroke-width="2.4" stroke-linecap="round" stroke-linejoin="round"/></svg>Shoes and Leather Repairs by Pelham Brothers</li>
    <li><svg viewBox="0 0 18 14"><path d="M1 8 L6 12 L17 2" fill="none" stroke="var(--gold)" stroke-width="2.4" stroke-linecap="round" stroke-linejoin="round"/></svg>Area Rug Cleaning by Tarrick Cleaners</li>
    <li><svg viewBox="0 0 18 14"><path d="M1 8 L6 12 L17 2" fill="none" stroke="var(--gold)" stroke-width="2.4" stroke-linecap="round" stroke-linejoin="round"/></svg>Leather and Suede Cleaning by Mosk Cleaners</li>
    <li><svg viewBox="0 0 18 14"><path d="M1 8 L6 12 L17 2" fill="none" stroke="var(--gold)" stroke-width="2.4" stroke-linecap="round" stroke-linejoin="round"/></svg>Household Items</li>
    <li><svg viewBox="0 0 18 14"><path d="M1 8 L6 12 L17 2" fill="none" stroke="var(--gold)" stroke-width="2.4" stroke-linecap="round" stroke-linejoin="round"/></svg>Wedding Dress Cleaning and Preservation</li>
  </ul>

  <div class="abs coupon">
    <div class="coupon-title">COUPON</div>
    <div>NEW CUSTOMERS:</div>
    <div class="coupon-value">20% OFF</div>
    <div>YOUR FIRST SERVICE.</div>
    <div class="coupon-gap"></div>
    <div>EVERYONE:</div>
    <div class="coupon-value">10% OFF</div>
    <div>(ONE-TIME USE)</div>
  </div>

  <div class="abs phone-tab">
    <svg viewBox="0 0 24 24"><path d="M6.6 10.8a15.1 15.1 0 0 0 6.6 6.6l2.2-2.2a1 1 0 0 1 1-.25 11.4 11.4 0 0 0 3.6.57 1 1 0 0 1 1 1V20a1 1 0 0 1-1 1A17 17 0 0 1 3 4a1 1 0 0 1 1-1h3.5a1 1 0 0 1 1 1c0 1.250.2 2.45.57 3.6a1 1 0 0 1-.25 1Z" fill="var(--navy)"/></svg>
    555-014-2290
  </div>
</section>

<section class="card card-back" aria-label="Postcard back">
  <svg class="shapes" viewBox="0 0 840 560" aria-hidden="true">
    <path d="M330 0 H440 Q480 140 455 300 L420 300 Q430 120 330 0 Z" fill="var(--navy)"/>
    <path d="M0 0 H340 Q465 120 460 290 Q455 450 305 560 H0 Z" fill="var(--gold-deep)"/>
  </svg>

  <h2 class="abs about-title">ABOUT US:</h2>
  <div class="abs about-copy">
    <p>Vantor Cleaners is a premium dry cleaning and garment care service dedicated to delivering exceptional quality, convenience, and personalized attention. Located in the heart of Corwin Falls, NJ, we specialize in eco-friendly drycleaning, expert stain removal, professional garment pressing, and specialized care for delicate fabrics, designer clothing, household items, and formal wear.</p>
    <p>Our mission is to provide reliable, high-quality service while preserving the longevity and appearance of our customers’ garments. With state-of-the-art equipment, experienced staff, and a commitment to customer satisfaction, Vantor Cleaners ensures your clothing looks and feels its best - every time.</p>
    <p>We also offer convenient services such as same-day cleaning, alterations, wash &amp; fold, and pickup and delivery options, making garment care simple and hassle-free for our busy clientele.</p>
    <p>Experience the difference with Vantor Cleaners - where luxury care meets everyday convenience.</p>
  </div>

  <div class="abs call-label">CALL NOW:</div>
  <div class="abs call-number">
    <svg viewBox="0 0 24 24"><path d="M6.6 10.8a15.1 15.1 0 0 0 6.6 6.6l2.2-2.2a1 1 0 0 1 1-.25 11.4 11.4 0 0 0 3.6.57 1 1 0 0 1 1 1V20a1 1 0 0 1-1 1A17 17 0 0 1 3 4a1 1 0 0 1 1-1h3.5a1 1 0 0 1 1 1c0 1.25.2 2.45.57 3.6a1 1 0 0 1-.25 1Z" fill="var(--navy)"/></svg>
    555-014-2290
  </div>

  <div class="abs stamp-box" aria-label="Stamp area"></div>
  <div class="abs address-line" style="top:200px"></div>
  <div class="abs address-line" style="top:257px"></div>

  <div class="abs map-address">18 LINDEN RIDGE<br>ROAD CORWIN FALLS,<br>NJ 07990</div>
  <div class="abs map-area" role="img" aria-label="Street map of Linden Ridge Rd showing the store location beside Corsello's Pizza &amp; Pasta and Lumen Hair"></div>
</section>

</body>
</html>
```